Velbrin Industries Digital Flyer

Digital Flyers for a machine shop, preferably PDF format.

Looking for a futuristic look/layout

Target Market(s)

Tier 1 and 2 Military, Defense contractors, Medical, Space, Microsatellite

Industry/Entity Type

Ultra-high precision machining of complex, mission critical components. Primary industries are defense, aerospace, space, micro-satellites, satellites

Font styles to use
Serif

Colors
0054AA
0677BA
7BADD7
CADEEF
E8F1F8

```html
<!DOCTYPE html>
<html lang="en">
<head>
<meta charset="utf-8">
<title>Velbrin Industries Flyer</title>
<link href="https://fonts.googleapis.com/css2?family=Montserrat:wght@400;500;700;800&display=swap" rel="stylesheet">
<style>
  :root {
    --navy: #1b3149;
    --gold: #b8904f;
    --paper: #ffffff;
    --ink: #4a5563;
    --backdrop: #e4e4e4;
    --photo-light: #c9ced3;
    --photo-dark: #6e7780;
  }
  * { margin: 0; padding: 0; box-sizing: border-box; }
  html, body { width: 1200px; height: 1200px; overflow: hidden; }
  body {
    background: var(--backdrop);
    font-family: "Montserrat", sans-serif;
    color: var(--ink);
  }
  .flyer {
    position: absolute;
    left: 197px; top: 30px;
    width: 806px; height: 1140px;
    background: var(--paper);
    overflow: hidden;
    box-shadow: 0 6px 24px rgba(0,0,0,0.12);
  }
  .hero { position: absolute; left: 0; top: 0; width: 806px; height: 620px; }

  .brand {
    position: absolute; left: 450px; top: 440px;
    display: flex; align-items: center; gap: 14px;
  }
  .brand-dot { width: 44px; height: 44px; border-radius: 50%; background: var(--navy); }
  .brand-name {
    font-weight: 700; font-size: 26px; line-height: 1.05;
    color: var(--navy); letter-spacing: 0.5px; text-transform: uppercase;
  }

  .divider {
    position: absolute; left: 410px; top: 540px;
    width: 1px; height: 400px; background: var(--gold);
  }

  .sectors { position: absolute; left: 440px; top: 545px; width: 330px; list-style: none; }
  .sector { display: flex; gap: 16px; align-items: flex-start; margin-bottom: 30px; }
  .sector-icon {
    flex: none; width: 30px; height: 30px; border-radius: 6px;
    display: flex; align-items: center; justify-content: center; margin-top: 14px;
  }
  .sector-icon.gold { background: var(--gold); }
  .sector-icon.navy { background: var(--navy); }
  .sector-title { font-weight: 800; font-size: 16px; color: var(--navy); letter-spacing: 0.3px; }
  .sector-text { font-size: 11px; line-height: 1.5; margin-top: 3px; }

  .intro { position: absolute; left: 60px; top: 625px; width: 330px; }
  .intro-title { font-weight: 800; font-size: 40px; color: var(--navy); line-height: 1; }
  .intro-sub { font-size: 20px; color: var(--navy); margin-top: 4px; }
  .intro-body { font-size: 12px; line-height: 1.7; margin-top: 22px; letter-spacing: 0.4px; }

  .contact {
    position: absolute; left: 60px; top: 958px;
    display: flex; gap: 24px; font-size: 13px; letter-spacing: 0.5px;
  }
  .contact-item { display: flex; align-items: center; gap: 8px; }
  .contact-icon {
    width: 24px; height: 24px; border-radius: 6px; background: var(--navy);
    display: flex; align-items: center; justify-content: center;
  }

  .footer-rule {
    position: absolute; left: 0; top: 1000px; width: 806px; height: 3px; background: var(--navy);
  }
  .footer {
    position: absolute; left: 0; top: 1012px; width: 806px; height: 128px;
    background: var(--navy); color: #fff;
    display: flex; justify-content: flex-end; padding: 16px 50px 0 0;
    font-size: 14px; letter-spacing: 1px;
  }
</style>
</head>
<body>
<main class="flyer">
  <svg class="hero" viewBox="0 0 806 620" xmlns="http://www.w3.org/2000/svg">
    <defs>
      <linearGradient id="photoTone" x1="0" y1="0" x2="1" y2="1">
        <stop offset="0" stop-color="#c9ced3"/>
        <stop offset="0.6" stop-color="#9aa3ac"/>
        <stop offset="1" stop-color="#6e7780"/>
      </linearGradient>
    </defs>
    <path role="img" aria-label="Photo of workers in hard hats and safety vests operating a precision saw in a machine shop"
          d="M0,0 H806 V330 C700,300 560,330 470,420 C400,490 330,560 0,560 Z" fill="url(#photoTone)"/>
    <path d="M0,560 C330,560 400,490 470,420 L486,432 C410,520 330,592 0,592 Z" fill="#b8904f"/>
    <path d="M470,420 C560,330 700,300 806,330 V392 C700,362 585,380 505,440 Z" fill="#1b3149"/>
  </svg>

  <div class="brand">
    <span class="brand-dot"></span>
    <span class="brand-name">Velbrin<br>Industries</span>
  </div>

  <div class="divider"></div>

  <ul class="sectors">
    <li class="sector">
      <span class="sector-icon gold"><svg width="14" height="14" viewBox="0 0 14 14"><path d="M2 3 L7 7 L12 3 M2 7 L7 11 L12 7" stroke="#fff" stroke-width="2" fill="none"/></svg></span>
      <div><div class="sector-title">MILITARY</div><p class="sector-text">Lorem Ipsum is simply dummy text of the printing and typesetting industry.</p></div>
    </li>
    <li class="sector">
      <span class="sector-icon navy"><svg width="14" height="14" viewBox="0 0 14 14"><path d="M7 1 L12 3 V7 C12 10 9.5 12 7 13 C4.5 12 2 10 2 7 V3 Z" fill="#fff"/></svg></span>
      <div><div class="sector-title">DEFENSE CONTRACTOR</div><p class="sector-text">Lorem Ipsum is simply dummy text of the printing and typesetting industry.</p></div>
    </li>
    <li class="sector">
      <span class="sector-icon gold"><svg width="14" height="14" viewBox="0 0 14 14"><path d="M5 1 H9 V5 H13 V9 H9 V13 H5 V9 H1 V5 H5 Z" fill="#fff"/></svg></span>
      <div><div class="sector-title">MEDICAL</div><p class="sector-text">Lorem Ipsum is simply dummy text of the printing and typesetting industry.</p></div>
    </li>
    <li class="sector">
      <span class="sector-icon navy"><svg width="14" height="14" viewBox="0 0 14 14"><path d="M7 1 C9 3 10 6 9.5 10 H4.5 C4 6 5 3 7 1 Z M4.5 10 L2.5 13 M9.5 10 L11.5 13" stroke="#fff" stroke-width="1.5" fill="#fff"/></svg></span>
      <div><div class="sector-title">SPACE</div><p class="sector-text">Lorem Ipsum is simply dummy text of the printing and typesetting industry.</p></div>
    </li>
    <li class="sector">
      <span class="sector-icon gold"><svg width="14" height="14" viewBox="0 0 14 14"><path d="M5 1 H9 M6 1 V5 L2 12 H12 L8 5 V1" stroke="#fff" stroke-width="1.6" fill="none"/></svg></span>
      <div><div class="sector-title">MICROSATELLITE</div><p class="sector-text">Lorem Ipsum is simply dummy text of the printing and typesetting industry.</p></div>
    </li>
  </ul>

  <section class="intro">
    <h1 class="intro-title">LOREM IPSUM</h1>
    <p class="intro-sub">is simply dummy text</p>
    <p class="intro-body">Lorem Ipsum is simply dummy text of the printing and typesetting industry. Lorem Ipsum has been the industry's standard dummy text ever since the 1500s, when an unknown printer took a galley of type and scrambled it to make a type specimen book.</p>
    <p class="intro-body">Lorem Ipsum is simply dummy text of the printing and typesetting industry. Lorem Ipsum has been the industry's standard dummy text.</p>
  </section>

  <div class="contact">
    <span class="contact-item">
      <span class="contact-icon"><svg width="12" height="12" viewBox="0 0 12 12"><path d="M2 1 L4.5 1 L5.5 4 L4 5 C4.7 6.6 5.4 7.3 7 8 L8 6.5 L11 7.5 V10 C11 10.6 10.6 11 10 11 C5 11 1 7 1 2 C1 1.4 1.4 1 2 1 Z" fill="#fff"/></svg></span>
      000.000.000
    </span>
    <span class="contact-item">
      <span class="contact-icon"><svg width="12" height="12" viewBox="0 0 12 12"><rect x="1" y="2.5" width="10" height="7" fill="none" stroke="#fff" stroke-width="1.3"/><path d="M1 3 L6 7 L11 3" fill="none" stroke="#fff" stroke-width="1.3"/></svg></span>
      info@velbrin-ind.com
    </span>
  </div>

  <div class="footer-rule"></div>
  <footer class="footer">www.velbrin-ind.com</footer>
</main>
</body>
</html>
```